One page website

I'm looking for a landing page for my company. Just a brief description of our medical device technology with some images

Coding

Coded - Design and coding required

```html
<!DOCTYPE html>
<html lang="en">
<head>
<meta charset="utf-8">
<title>Veridan Surgical</title>
<link rel="stylesheet" href="https://fonts.googleapis.com/css2?family=Poppins:wght@300;400;500&family=Roboto:wght@300;400;500;700;900&display=swap">
<style>
:root{
  --blue:#1a9ad6;
  --green:#8dc63f;
  --teal:#3aa9b9;
  --ink:#1e1e1e;
  --body:#2b2b2b;
  --muted:#6b6b6b;
  --grey-band:#f2f2f2;
  --footer:#231f20;
  --footer-text:#b7b7b7;
  --white:#ffffff;
}
*{margin:0;padding:0;box-sizing:border-box}
html,body{width:1200px;height:2747px;overflow:hidden;background:var(--white)}
body{position:relative;font-family:'Roboto',sans-serif;color:var(--body)}
.abs{position:absolute}

/* header */
.site-header{position:absolute;left:0;top:0;width:1200px;height:83px;background:rgba(255,255,255,.9);z-index:5;box-shadow:0 1px 3px rgba(0,0,0,.06)}
.brand{position:absolute;left:117px;top:26px;font-family:'Poppins',sans-serif;font-weight:500;font-size:22px;color:var(--green);display:flex;align-items:center;gap:7px}
.brand-dot{width:10px;height:10px;border-radius:50%;background:var(--green)}
.nav a{position:absolute;top:32px;font-size:18px;color:#333;text-decoration:none}
.nav a.active{color:var(--blue);padding-bottom:6px;border-bottom:2px solid var(--blue)}
.btn-touch{position:absolute;left:922px;top:25px;width:161px;height:37px;border-radius:19px;background:var(--green);color:#fff;font-family:'Poppins',sans-serif;font-weight:500;font-size:14.5px;display:flex;align-items:center;justify-content:center}

/* hero */
.hero-media{position:absolute;left:0;top:0;width:1200px;height:603px;background:linear-gradient(100deg,#d9dde2 0%,#e7e9ec 40%,#c7ccd3 70%,#eef0f2 100%);clip-path:polygon(0 0,100% 0,100% 565px,597px 603px,0 565px)}
.hero-title{position:absolute;left:164px;top:186px;font-weight:900;font-size:74px;color:var(--blue);letter-spacing:-1px;line-height:1}
.hero-sub{position:absolute;left:164px;top:266px;font-weight:300;font-size:57px;color:#111;line-height:1;letter-spacing:-.5px}
.hero-lead{position:absolute;left:164px;top:353px;font-size:17px;color:#111;letter-spacing:-.2px}
.btn-learn{position:absolute;left:162px;top:414px;width:160px;height:37px;border-radius:19px;background:var(--green);color:#fff;font-family:'Poppins',sans-serif;font-size:16px;display:flex;align-items:center;justify-content:center}
.slide-arrow{position:absolute;top:282px;width:53px;height:42px;background:#fff;display:flex;align-items:center;justify-content:center}

/* what we do */
.grey-band{position:absolute;left:0;top:995px;width:1200px;height:598px;background:var(--grey-band);clip-path:polygon(0 0,100% 0,100% 498px,0 584px)}
.section-title{position:absolute;left:0;width:1200px;text-align:center}
.wwd-title{top:650px;font-size:42px;font-weight:500;color:#111;letter-spacing:-.5px}
.wwd-title span{color:var(--green);font-weight:400}
.wwd-text{position:absolute;left:280px;top:716px;width:640px;text-align:center;font-size:17px;line-height:30px;color:#222;letter-spacing:-.2px}
.card{position:absolute;top:843px;width:264px;height:250px;background:#fff;border:1px solid #e6e6e6;border-radius:3px;text-align:center;font-family:'Poppins',sans-serif}
.card svg{margin-top:26px}
.card h3{font-size:16px;font-weight:500;color:#222;margin-top:10px}
.card p{font-size:12px;color:#666;line-height:21px;margin-top:10px}
.card .more{font-size:12px;color:#555;margin-top:14px;display:block}
.card.featured{background:var(--green);border-color:var(--green)}
.card.featured h3,.card.featured p,.card.featured .more{color:#fff}

/* benefits */
.benefit-title{font-size:33px;font-weight:700;color:#222;letter-spacing:-.6px}
.benefit{position:absolute;font-family:'Poppins',sans-serif;font-size:16.5px;line-height:30px;color:#222}
.benefit-icon{position:absolute}

/* team */
.team-band{position:absolute;left:0;top:2032px;width:1200px;height:423px;background:var(--grey-band)}
.team-title{top:2096px;font-family:'Poppins',sans-serif;font-weight:300;font-size:31px;color:#222;letter-spacing:1px}
.member-photo{position:absolute;width:72px;height:72px;border-radius:50%;background:radial-gradient(circle at 50% 40%,#c9a58c,#6d6f7a 70%)}
.member-text{position:absolute;font-size:11.5px;line-height:14px;color:#333}
.member-text .name{font-size:14.5px;font-weight:500;color:#111}
.member-text .role{font-size:15px;color:var(--blue);line-height:17px;margin-bottom:9px}
.member-text p{margin-bottom:9px}
.dot{position:absolute;top:2403px;width:12px;height:12px;border-radius:50%;background:#c8c8c8}
.dot.active{background:var(--green)}

/* footer */
.site-footer{position:absolute;left:0;top:2455px;width:1200px;height:292px;background:var(--footer);color:var(--footer-text);font-size:14px}
.f-head{position:absolute;color:#fff;font-size:16px}
.f-col{position:absolute;line-height:26px}
.f-rule{position:absolute;width:1px;height:144px;background:#3c3839;top:54px}
.f-input{position:absolute;left:661px;top:145px;width:417px;height:37px;border-radius:19px;background:#edf2f6;overflow:hidden}
.f-input span{position:absolute;left:25px;top:10px;color:#8a8f95;font-size:14px}
.f-input b{position:absolute;right:0;top:0;width:127px;height:37px;background:var(--blue);color:#fff;font-weight:500;font-size:14.5px;display:flex;align-items:center;justify-content:center}
.f-line{position:absolute;left:0;top:228px;width:1200px;height:1px;background:#3c3839}
.copyright{position:absolute;left:0;top:252px;width:1200px;text-align:center;font-size:13.5px}
</style>
</head>
<body>

<div class="hero-media" role="img" aria-label="Physiotherapist guiding a young girl through a spine exercise on an exercise ball in a bright clinic"></div>

<header class="site-header">
  <div class="brand"><span class="brand-dot"></span>Veridan Surgical</div>
  <nav class="nav">
    <a href="#" class="active" style="left:458px">Home</a>
    <a href="#" style="left:563px">About</a>
    <a href="#" style="left:668px">Services</a>
    <a href="#" style="left:789px">Treatment</a>
  </nav>
  <div class="btn-touch">Get In Touch</div>
</header>

<div class="slide-arrow" style="left:86px"><svg width="10" height="14" viewBox="0 0 10 14"><path d="M7 2 2 7l5 5" fill="none" stroke="var(--blue)" stroke-width="1.5"/></svg></div>
<div class="slide-arrow" style="left:1061px"><svg width="10" height="14" viewBox="0 0 10 14"><path d="M3 2l5 5-5 5" fill="none" stroke="var(--blue)" stroke-width="1.5"/></svg></div>

<h1 class="hero-title">SOLVING</h1>
<div class="hero-sub">Children’s Scoliosis</div>
<p class="hero-lead">Develop novel technologies focusing on non-fusion scoliosis</p>
<div class="btn-learn">Learn More</div>

<div class="grey-band"></div>

<h2 class="section-title wwd-title">What <span>We Do</span></h2>
<p class="wwd-text">Develop novel technologies focusing on non-fusion scoliosis correction allowing for<br>non-surgical dynamic adjustment of implants over time.</p>

<div class="card" style="left:178px">
  <svg width="70" height="66" viewBox="0 0 70 66" fill="none" stroke="var(--teal)" stroke-width="2"><circle cx="35" cy="9" r="6"/><path d="M8 34h58v10H8z M14 44v18 M60 44v18 M26 34l8-16 10 6 6 10"/><path d="M30 44v14 M40 44v14 M50 44v14" stroke="var(--green)"/></svg>
  <h3>Monitoring Treatment</h3>
  <p>Lorem Ipsum is simply dummy<br>and typesetting</p>
  <span class="more">Read More &nbsp;›</span>
</div>
<div class="card featured" style="left:469px">
  <svg width="70" height="66" viewBox="0 0 70 66" fill="none" stroke="#fff" stroke-width="2"><path d="M20 6c-6 8-8 30-4 56 M50 6c6 8 8 30 4 56"/><rect x="30" y="8" width="10" height="8" rx="2"/><rect x="30" y="20" width="10" height="8" rx="2"/><rect x="30" y="32" width="10" height="8" rx="2"/><rect x="30" y="44" width="10" height="8" rx="2"/></svg>
  <h3>Bracing Treatment</h3>
  <p>Lorem Ipsum is simply dummy<br>and typesetting</p>
  <span class="more">Read More &nbsp;›</span>
</div>
<div class="card" style="left:758px">
  <svg width="76" height="66" viewBox="0 0 76 66" fill="none" stroke="var(--teal)" stroke-width="2"><circle cx="38" cy="12" r="7"/><path d="M6 8l20 16h24l20-16 M26 24v12 M50 24v12"/><path d="M4 42c8-5 14 5 22 0s14 5 22 0 14 5 22 0 M4 52c8-5 14 5 22 0s14 5 22 0 14 5 22 0 M4 62c8-5 14 5 22 0s14 5 22 0 14 5 22 0" stroke="var(--green)"/></svg>
  <h3>Fusion Treatment</h3>
  <p>Lorem Ipsum is simply dummy<br>and typesetting</p>
  <span class="more">Read More &nbsp;›</span>
</div>

<h2 class="section-title benefit-title" style="top:1183px">BENEFITS - ADVANTAGES OF VBT OVER FUSION</h2>

<svg class="benefit-icon" style="left:181px;top:1270px" width="56" height="60" viewBox="0 0 56 60" fill="none" stroke="var(--green)" stroke-width="2"><path d="M6 58V44h8v14 M20 58V36h8v22 M34 58V28h8v30" stroke="var(--teal)"/><path d="M4 34l16-12 10 6 20-20 M42 6h8v8"/></svg>
<div class="benefit" style="left:269px;top:1291px">Continued skeletal growth</div>
<svg class="benefit-icon" style="left:631px;top:1270px" width="64" height="62" viewBox="0 0 64 62" fill="none" stroke="var(--teal)" stroke-width="2"><circle cx="50" cy="8" r="6" stroke="var(--green)"/><path d="M26 20l14-4 6 12 10 2 M40 16l-8 22 10 10-4 12 M32 38l-12 4-12 2 M22 26l-14 2 M2 36h10"/></svg>
<div class="benefit" style="left:719px;top:1282px">Partial Motion Preservation</div>

<svg class="benefit-icon" style="left:181px;top:1386px" width="60" height="64" viewBox="0 0 60 64" fill="none" stroke="var(--teal)" stroke-width="2"><path d="M4 2v52 M4 42h52v-8H4 M10 54h44 M14 54v6 M50 54v6"/><rect x="12" y="4" width="8" height="12" rx="2" stroke="var(--green)"/><path d="M16 16v16" stroke="var(--green)"/><circle cx="14" cy="36" r="4"/></svg>
<div class="benefit" style="left:269px;top:1403px">Single treatment event</div>
<svg class="benefit-icon" style="left:631px;top:1386px" width="62" height="62" viewBox="0 0 62 62" fill="none" stroke="var(--teal)" stroke-width="2"><circle cx="9" cy="6" r="4" stroke="var(--green)"/><circle cx="52" cy="8" r="4" stroke="var(--green)"/><path d="M4 16h10v30 M58 18H48v30 M14 28h34 M20 20h22v24H20z M6 60V30 M56 60V32"/></svg>
<div class="benefit" style="left:719px;top:1396px">Little impact on activity<br>and appearance</div>

<h2 class="section-title benefit-title" style="top:1665px">BENEFITS - VBT HAS PROVEN RESULTS</h2>

<svg class="benefit-icon" style="left:178px;top:1745px" width="64" height="66" viewBox="0 0 64 66" fill="none" stroke="var(--teal)" stroke-width="2"><circle cx="32" cy="30" r="12" stroke="var(--green)"/><path d="M32 2v8 M24 4v6 M40 4v6" stroke="var(--green)"/><path d="M2 46h10v18H2z M12 48h16c6 0 10 4 12 6h10l12-8 M12 60h34l14-10"/><text x="28" y="35" font-size="14" fill="var(--teal)" stroke="none" font-family="Roboto">$</text></svg>
<div class="benefit" style="left:270px;top:1755px">~66% Cost Savings ($50K<br>compared to $150K)</div>
<svg class="benefit-icon" style="left:632px;top:1745px" width="64" height="64" viewBox="0 0 64 64" fill="none" stroke="var(--teal)" stroke-width="2"><circle cx="32" cy="20" r="16" stroke="var(--green)"/><path d="M32 12v9h7" stroke="var(--green)"/><path d="M4 26c0 14 8 22 18 30 M60 26c0 14-8 22-18 30 M10 40l12 10 M54 40L42 50"/></svg>
<div class="benefit" style="left:721px;top:1754px">50% Saving in Surgery Time<br>(1.5-2 hrs compared to 4-6 hrs)</div>

<svg class="benefit-icon" style="left:182px;top:1866px" width="60" height="64" viewBox="0 0 60 64" fill="none" stroke="var(--teal)" stroke-width="2"><path d="M4 2v52 M4 42h52v-8H4 M10 54h44 M14 54v6 M50 54v6"/><rect x="12" y="4" width="8" height="12" rx="2" stroke="var(--green)"/><path d="M16 16v16" stroke="var(--green)"/><circle cx="14" cy="36" r="4"/></svg>
<div class="benefit" style="left:270px;top:1877px">50% Saving in Hospital Stay<br>(2-3 days compared to 6-7 days)</div>
<svg class="benefit-icon" style="left:636px;top:1876px" width="60" height="60" viewBox="0 0 60 60" fill="none" stroke="var(--teal)" stroke-width="2"><path d="M52 18A26 26 0 0 0 8 20 M8 42a26 26 0 0 0 44-2 M52 8v10H42 M8 52V42h10"/><path d="M20 28h6v14h-6z M26 30l6-10c3 0 4 2 3 6h8c2 0 3 2 2 4l-3 10c-1 2-2 2-4 2H26" stroke="var(--green)"/></svg>
<div class="benefit" style="left:721px;top:1878px">Confirmed improved self-<br>confidence for surgical recipients</div>

<div class="team-band"></div>
<h2 class="section-title team-title">OUR TEAM</h2>

<svg class="abs" style="left:155px;top:2181px" width="90" height="90" viewBox="0 0 90 90" fill="none" stroke="var(--green)" stroke-width="2"><path d="M45 2a43 43 0 1 1-42 34"/><path d="M45 8a37 37 0 1 0 36 28"/></svg>
<div class="member-photo" style="left:164px;top:2190px" role="img" aria-label="Portrait of the founder"></div>
<div class="member-text" style="left:260px;top:2180px">
  <div class="name">Daniel Hoyle</div>
  <div class="role">Founder and CEO</div>
  <p>Co-founder and CEO<br>of Linecrest Innovations-<br>Acquired by Halvern<br>in 2014</p>
  <p>Leadership positions at<br>Quorvane Labs and Castell</p>
</div>

<svg class="abs" style="left:459px;top:2181px" width="90" height="90" viewBox="0 0 90 90" fill="none" stroke="var(--green)" stroke-width="2"><path d="M45 2a43 43 0 1 1-42 34"/><path d="M45 8a37 37 0 1 0 36 28"/></svg>
<div class="member-photo" style="left:468px;top:2190px" role="img" aria-label="Portrait of the co-founder"></div>
<div class="member-text" style="left:564px;top:2180px">
  <div class="name">Arjun Mehta Ph.D.</div>
  <div class="role">Co-Founder Chief<br>Science Officer</div>
  <p>Previous Chief Science<br>Officer at Linecrest<br>Innovations</p>
  <p>Previous leadership<br>positions at Spinewell,<br>Halvern and Orthavia</p>
</div>

<svg class="abs" style="left:791px;top:2182px" width="90" height="90" viewBox="0 0 90 90" fill="none" stroke="var(--green)" stroke-width="2"><path d="M45 2a43 43 0 1 1-42 34"/><path d="M45 8a37 37 0 1 0 36 28"/></svg>
<div class="member-photo" style="left:800px;top:2191px" role="img" aria-label="Portrait of the co-founder"></div>
<div class="member-text" style="left:897px;top:2181px">
  <div class="name">Arjun Mehta Ph.D.</div>
  <div class="role">Co-Founder Chief<br>Science Officer</div>
  <p>Previous Chief Science<br>Officer at Linecrest<br>Innovations</p>
  <p>Previous leadership<br>positions at Spinewell,<br>Halvern and Orthavia</p>
</div>

<span class="dot" style="left:567px"></span>
<span class="dot active" style="left:594px"></span>
<span class="dot" style="left:621px"></span>

<footer class="site-footer">
  <div class="f-head" style="left:118px;top:51px">Contact Us</div>
  <div class="f-col" style="left:118px;top:89px">Lorem Ipsum,<br>is simply dummy text of</div>
  <div class="f-col" style="left:118px;top:153px">xxx xxx xxxx</div>
  <div class="f-col" style="left:118px;top:185px">xxxxxxx@mailbox.com</div>
  <div class="f-rule" style="left:332px"></div>
  <div class="f-head" style="left:415px;top:51px">Contact Us</div>
  <div class="f-col" style="left:415px;top:88px">Home<br>About<br>Services<br>Contact</div>
  <div class="f-rule" style="left:575px"></div>
  <div class="f-head" style="left:661px;top:52px">Email Newsletters</div>
  <div class="f-col" style="left:661px;top:89px">Keep me up to date with content, updates, and offers from veridan</div>
  <div class="f-input"><span>Email address</span><b>Subscribe</b></div>
  <div class="f-line"></div>
  <div class="copyright">Copyright Veridan Surgical. All right reserved.</div>
</footer>

</body>
</html>
```